Steel Company / Iron Railing Business Card Template

We are a custom steel fabrication company located in Ashwick, PN. In business since 1979, we recently developed a new logo, and we're looking for a business card design to help display the new logo and our business. The name of the company is Kelbrook Forge Co.. The Office Phone number is (610) 555-0143. We fabricate and install custom "wrought iron" railings on our residential side, we also fabricate and erect structural steel (think cranes and steel beams in buildings) on our commercial side. Looking to get a business card template designed. Something modern, but professional. Clear and easy to read. Front should have all business and employee information including phone number(s), email address, business information, etc. back should spotlight logo.

Industry/Entity Type

Construction / Home Improvement

Contact Information for Business Card

Business information is Kelbrook Forge Co., 48 Dunmore Ave Suite 3305, Ashwick, PN 19074. Phone number is (610) 555-0143. Website is www.kelbrookforge.example Business card should be for "Tom Pelling" with the job title "Sales & Estimating" but be editable for other employees. Tom's phone number is (610) 555-0178

Colors

Designer to choose colors to be used in the design.

Requirements
Must have
• Modern Feel, Design should be sized for standard business card sizing 3.5" x 2" (88.9mm x 50.8mm)

```html
<!DOCTYPE html>
<html lang="en">
<head>
<meta charset="utf-8">
<title>Kelbrook Forge Co. – Business Card</title>
<link rel="stylesheet" href="https://fonts.googleapis.com/css2?family=Montserrat:wght@400;500;700;800&display=swap">
<style>
  :root {
    --brand-blue: #22418f;
    --brand-blue-deep: #1b3478;
    --brand-red: #d1282e;
    --card-white: #ffffff;
    --ink: #2a2a2a;
    --stage: #3a3a3a;
  }
  * { box-sizing: border-box; margin: 0; padding: 0; }
  html, body { width: 1200px; height: 875px; overflow: hidden; }
  body {
    background: var(--stage);
    font-family: "Montserrat", sans-serif;
    display: flex;
    align-items: center;
    justify-content: center;
    gap: 50px;
  }
  .card {
    position: relative;
    width: 525px;
    height: 300px;
    border-radius: 20px;
    overflow: hidden;
    box-shadow: 0 14px 30px rgba(0,0,0,0.45);
  }
  /* Back of card */
  .card-back {
    background: var(--brand-blue);
    display: flex;
    align-items: center;
    justify-content: center;
    gap: 14px;
  }
  .card-back .mark-circle {
    flex: none;
    width: 40px; height: 40px;
    border-radius: 50%;
    background: var(--brand-blue-deep);
  }
  .card-back .wordmark {
    color: var(--brand-blue-deep);
    font-weight: 800;
    font-size: 36px;
    line-height: 1;
    white-space: nowrap;
  }
  /* Front of card */
  .card-front { background: var(--card-white); }
  .front-bands { position: absolute; inset: 0; }
  .brand-block {
    position: absolute;
    left: 32px; top: 92px;
    display: flex; align-items: center; gap: 8px;
    width: 170px;
  }
  .brand-block .mark-circle {
    flex: none;
    width: 16px; height: 16px;
    border-radius: 50%;
    background: var(--brand-red);
  }
  .brand-block .wordmark {
    color: var(--brand-blue);
    font-weight: 800;
    font-size: 19px;
    line-height: 1.1;
  }
  .divider {
    position: absolute;
    left: 216px; top: 62px;
    width: 1.5px; height: 110px;
    background: var(--brand-blue);
  }
  .contact {
    position: absolute;
    left: 234px; top: 58px;
  }
  .person-name {
    color: var(--brand-blue);
    font-weight: 800;
    font-size: 22px;
    line-height: 1.1;
  }
  .person-title {
    color: var(--ink);
    font-size: 12px;
    font-weight: 500;
    margin-bottom: 9px;
  }
  .contact-list { list-style: none; }
  .contact-list li {
    display: flex; align-items: center; gap: 7px;
    color: var(--ink);
    font-size: 12px;
    line-height: 1.6;
    white-space: nowrap;
  }
  .contact-list svg { width: 11px; height: 11px; fill: var(--brand-blue); flex: none; }
  .address {
    position: absolute;
    left: 0; top: 210px;
    width: 455px; height: 40px;
    display: flex; align-items: center; justify-content: center;
    color: var(--card-white);
    font-size: 12.5px;
    font-weight: 500;
    letter-spacing: 0.2px;
    white-space: nowrap;
  }
</style>
</head>
<body>
  <section class="card card-back" aria-label="Card back">
    <span class="mark-circle"></span>
    <span class="wordmark">Kelbrook Forge Co.</span>
  </section>

  <section class="card card-front" aria-label="Card front">
    <svg class="front-bands" viewBox="0 0 525 300" aria-hidden="true">
      <polygon points="0,210 455,210 440,250 0,250" fill="var(--brand-blue)"/>
      <polygon points="472,168 525,168 525,206 456,206" fill="var(--brand-red)"/>
    </svg>

    <div class="brand-block">
      <span class="mark-circle"></span>
      <span class="wordmark">Kelbrook Forge Co.</span>
    </div>

    <div class="divider"></div>

    <div class="contact">
      <p class="person-name">Tom Pelling</p>
      <p class="person-title">Sales &amp; Estimating</p>
      <ul class="contact-list">
        <li>
          <svg viewBox="0 0 24 24"><path d="M6.6 10.8a15.1 15.1 0 0 0 6.6 6.6l2.2-2.2a1 1 0 0 1 1-.25 11.4 11.4 0 0 0 3.6.57 1 1 0 0 1 1 1V20a1 1 0 0 1-1 1A17 17 0 0 1 3 4a1 1 0 0 1 1-1h3.5a1 1 0 0 1 1 1c0 1.25.2 2.45.57 3.57a1 1 0 0 1-.25 1z"/></svg>
          (610) 555-0178
        </li>
        <li>
          <svg viewBox="0 0 24 24"><path d="M4 9h16l-2-4H6zM3 10h18v10H3zM8 13h2v2H8zm3 0h2v2h-2zm3 0h2v2h-2zM8 16h2v2H8zm3 0h2v2h-2zm3 0h2v2h-2z"/></svg>
          (610) 555-0143
        </li>
        <li>
          <svg viewBox="0 0 24 24"><path d="M12 2a10 10 0 1 0 0 20 10 10 0 0 0 0-20zm6.9 6h-2.9a15.7 15.7 0 0 0-1.4-3.6A8 8 0 0 1 18.9 8zM12 4c.8 1.2 1.5 2.5 1.9 4h-3.8c.4-1.5 1.100-2.8 1.9-4zM4.3 14a8.2 8.2 0 0 1 0-4h3.4a16 16 0 0 0 0 4zm.8 2h2.9c.3 1.3.8 2.5 1.4 3.6A8 8 0 0 1 5.1 16zM8 8H5.1a8 8 0 0 1 4.3-3.6C8.8 5.5 8.3 6.7 8 8zm4 12c-.8-1.2-1.5-2.5-1.9-4h3.8c-.4 1.5-1.1 2.8-1.900 4zm2.3-6H9.7a14.6 14.6 0 0 1 0-4h4.6a14.6 14.6 0 0 1 0 4zm.3 5.6c.6-1.1 1.1-2.3 1.4-3.6h2.9a8 8 0 0 1-4.3 3.6zm1.7-5.6a16 16 0 0 0 0-4h3.4a8.2 8.2 0 0 1 0 4z"/></svg>
          www.kelbrookforge.example
        </li>
      </ul>
    </div>

    <p class="address">48 Dunmore Ave Suite 3305 Ashwick, PN 19074</p>
  </section>
</body>
</html>
```